"Het Zaakkompas" needs a new Web Design

We need a web design for to support the startup of a new Activity.

Het Zaakkompas is a company that offers consulting services towards SMB based in Belgium. Focus of the consultancy is:
-Marketing
-Sales
-ICT

We would like to see designs that use the color blue and that fit's with our logo.

The website should communicate trust and expertise.

Main goal of the website is to attract new professional customers

We think of providing following content on the site:
-Home Page
-Who we are (present our 3 team members)
-How we work
-Skills we offer
-Contact us
-Groeiateliers (Free workshops we offer on a regular base)
-Blog

In a later stage:
-Testimonials
-Create & Integrate an animation where we present our services

Call To Actions:
-Register for our newsletter
-Register for a Groeiatelier
-Ask a free intake meeting

CTA's will change from time to time.
Design has to be responsive

Site will be made in wordpress. Design should fit in a existing template so we do not have to start from scratch.

see www.zaakkompas.be

The logo attached is just new. Feel free if yoy have any suggestions to approve this!

Target Market(s)

SMB companies that likes to grow and and expand there business

Industry/Entity Type

Management Consulting

Contact Information for Business Card

I was thinking of including there a picture in from ourselves

Coding

Coded - Design and coding required

Number of Pages Required

5+ page

Font styles to use
Sans Serif

Colors
3277b5
0592cd
33a6d7
85cae6
85acd2
fcfafc

Requirements
Must have
• I'm using the themes from Velvet Layouts
• For example Orla. Should nice tu use this.
• http://www.velvetlayouts.com/gallery/orla/
• I like the design from this site.
• http://www.ondernemershulp-veldhoek.be/#home
• Header menu can better but the thing I realy like is the design of the "Missie" page. the "animation"
Should not have
• I do not want a traditional design.
• Other sites I like:
• https://www.mailpeloton.com/
• https://www.staylantern.com
• https://www.tallygrove.com
• http://www.voxtrellis.com
• http://www.craftbazaru.com/

```html
<!DOCTYPE html>
<html lang="en">
<head>
<meta charset="utf-8">
<title>Het Zaakkompas — Consulting towards SMB</title>
<link href="https://fonts.googleapis.com/css2?family=Open+Sans:wght@400;600;700;800&display=swap" rel="stylesheet">
<style>
:root{
  --navy:#1b3f6e;
  --navy-deep:#15345d;
  --blue:#3277b5;
  --blue-bright:#0592cd;
  --blue-soft:#33a6d7;
  --blue-pale:#85cae6;
  --blue-mute:#85acd2;
  --paper:#fcfafc;
  --ink:#333a44;
  --ink-soft:#7a818b;
  --footer:#2c2d30;
  --footer-bottom:#222326;
  --footer-text:#9a9ca1;
}
*{box-sizing:border-box;margin:0;padding:0}
html,body{width:1200px;height:2432px;overflow:hidden}
body{font-family:"Open Sans",Arial,sans-serif;color:var(--ink);background:#fff;font-size:13px;line-height:1.6}
.wrap{width:1000px;margin:0 auto;position:relative;height:100%}
section,header,footer{position:relative;width:1200px}

/* header */
.site-header{height:72px;background:#fff;border-bottom:1px solid #e6e8ec}
.brand{position:absolute;left:0;top:20px;display:flex;align-items:center;gap:10px}
.brand-mark{width:30px;height:30px;background:var(--blue)}
.brand-name{font-size:22px;font-weight:700;color:var(--navy);letter-spacing:.2px}
.main-nav{position:absolute;right:0;top:26px;display:flex;gap:38px;font-size:12px;color:#4a5058}
.main-nav a{color:inherit;text-decoration:none}
.main-nav a.active{color:var(--blue)}

/* hero */
.hero{height:468px;overflow:hidden}
.hero-photo{position:absolute;inset:0;background:linear-gradient(90deg,#1f5d98 0%,#4d86bb 30%,#9fbfd9 55%,#c9d7e4 75%,#b7c6d6 100%)}
.hero-copy{position:absolute;left:100px;top:236px;color:#fff}
.hero-kicker{font-size:24px;font-weight:700;letter-spacing:1px}
.hero-title{font-size:46px;font-weight:800;letter-spacing:1px;line-height:1.1;margin-top:2px}
.btn{display:inline-block;background:var(--navy);color:#fff;font-size:12px;padding:9px 20px;text-decoration:none}
.hero .btn{margin-top:28px}

/* cta band */
.cta-band{height:180px;background:var(--navy)}
.cta-row{position:absolute;left:0;top:22px;display:flex;gap:40px}
.cta-box{width:300px;height:138px;background:var(--blue);padding:18px 20px;display:grid;grid-template-columns:48px 1fr;column-gap:14px;color:#fff}
.cta-box:nth-child(2){background:#2a6aa6}
.cta-box:nth-child(3){background:var(--blue-soft)}
.cta-icon{width:44px;height:44px;border:2px solid #fff;border-radius:50%;display:flex;align-items:center;justify-content:center}
.cta-title{font-size:11px;font-weight:700;line-height:1.2;text-transform:uppercase}
.cta-title span{display:block;font-size:17px;font-weight:400}
.cta-text{grid-column:2;font-size:10.5px;line-height:1.5;color:#e3eef8;margin-top:8px}

/* welcome */
.welcome{height:220px;text-align:center}
.section-title{font-size:22px;font-weight:700;letter-spacing:1.5px;color:var(--navy);text-transform:uppercase}
.welcome .section-title{padding-top:56px}
.lead{font-size:12px;color:var(--ink-soft);width:840px;margin:14px auto 0;line-height:1.75}

/* services */
.services{height:380px}
.services-media{position:absolute;left:0;top:10px;width:460px;height:250px;background:linear-gradient(135deg,#8fb3d4,#c7d6e3 50%,#6f8fae);display:flex;align-items:center;justify-content:center}
.services-copy{position:absolute;left:500px;top:10px;width:500px}
.services-copy h3{font-size:18px;font-weight:700;color:var(--navy);text-transform:uppercase;letter-spacing:1px}
.services-copy .strong{font-weight:700;color:var(--ink);font-size:12px;margin-top:12px}
.services-copy p{font-size:11.5px;color:var(--ink-soft);margin-top:10px}
.services-copy .btn{margin-top:20px;background:var(--blue)}

/* info band */
.info-band{height:240px;background:linear-gradient(90deg,var(--navy-deep),var(--blue) 55%,#2f6fac)}
.info-col{position:absolute;top:40px;width:440px;color:#fff}
.info-col.right{left:540px}
.info-col h4{font-size:15px;font-weight:700;letter-spacing:1px;text-transform:uppercase}
.info-col p{font-size:11.5px;color:#d8e6f3;margin-top:12px}
.info-col a{display:inline-block;margin-top:14px;color:#fff;font-size:11.5px;text-decoration:none}
.info-divider{position:absolute;left:500px;top:36px;width:1px;height:150px;background:rgba(255,255,255,.25)}

/* offer */
.offer{height:520px;text-align:center}
.offer .section-title{padding-top:62px}
.offer-grid{position:absolute;left:0;top:180px;display:flex;gap:12px;text-align:left}
.offer-card{width:325px}
.offer-photo{height:160px}
.offer-card:nth-child(1) .offer-photo{background:linear-gradient(135deg,#6d87a6,#b9c6d4)}
.offer-card:nth-child(2) .offer-photo{background:linear-gradient(135deg,#a9b6c3,#dfe4ea)}
.offer-card:nth-child(3) .offer-photo{background:linear-gradient(135deg,#7a6a60,#c9bdb3)}
.offer-card h5{font-size:13px;font-weight:700;color:var(--navy);text-transform:uppercase;margin-top:18px;letter-spacing:.5px}
.offer-card p{font-size:11px;color:var(--ink-soft);margin-top:6px}

/* footer */
.site-footer{height:308px;background:var(--footer);color:var(--footer-text)}
.foot-col{position:absolute;top:44px}
.foot-col h6{font-size:12px;font-weight:700;color:#fff;text-transform:uppercase;letter-spacing:1px;margin-bottom:16px}
.foot-col ul{list-style:none;font-size:11px;line-height:2}
.testimonial{left:0;width:300px}
.quote{font-size:11px;line-height:1.7;padding-left:22px;position:relative}
.quote::before{content:"\201C";position:absolute;left:0;top:-6px;font-size:28px;color:var(--blue-soft)}
.author{display:flex;align-items:center;gap:12px;margin-top:18px}
.avatar{width:44px;height:44px;border-radius:50%;background:#6a6f77}
.author b{display:block;color:#fff;font-size:11px}
.author span{font-size:10px}
.col-welcome{left:380px}
.col-info{left:560px}
.col-follow{left:780px}
.col-follow li{display:flex;align-items:center;gap:10px;margin-bottom:6px}
.dot{width:22px;height:22px;border-radius:50%;border:1px solid #5b5e64}
.footer-bottom{height:44px;background:var(--footer-bottom);color:#777a80;font-size:10.5px;text-align:center;line-height:44px}
</style>
</head>
<body>

<header class="site-header">
  <div class="wrap">
    <div class="brand"><div class="brand-mark"></div><div class="brand-name">Het Zaakkompas</div></div>
    <nav class="main-nav">
      <a class="active" href="#">Home</a><a href="#">Who we are</a><a href="#">How we work</a><a href="#">Skills</a><a href="#">Groeiateliers</a><a href="#">Blog</a><a href="#">Contact us</a>
    </nav>
  </div>
</header>

<section class="hero">
  <div class="hero-photo" role="img" aria-label="Photo of smiling business consultants meeting at a desk in a bright office"></div>
  <div class="hero-copy">
    <div class="hero-kicker">WE OFFER CONSULTING SERVICES</div>
    <div class="hero-title">TOWARDS SMB</div>
    <a class="btn" href="#">View our history</a>
  </div>
</section>

<section class="cta-band">
  <div class="wrap">
    <div class="cta-row">
      <div class="cta-box">
        <div class="cta-icon"><svg width="22" height="16" viewBox="0 0 22 16"><rect x="1" y="1" width="20" height="14" fill="none" stroke="#fff" stroke-width="1.6"/><path d="M1 1l10 8 10-8" fill="none" stroke="#fff" stroke-width="1.6"/></svg></div>
        <div class="cta-title">Register for<span>OUR NEWSLETTER</span></div>
        <div class="cta-text">Stay informed on growth tips, upcoming workshops and news from our team, sent to your inbox every month.</div>
      </div>
      <div class="cta-box">
        <div class="cta-icon"><svg width="20" height="20" viewBox="0 0 20 20"><rect x="1" y="3" width="18" height="16" fill="none" stroke="#fff" stroke-width="1.6"/><path d="M1 8h18M6 1v4M14 1v4" stroke="#fff" stroke-width="1.6"/></svg></div>
        <div class="cta-title">Register for a<span>GROEIATELIER</span></div>
        <div class="cta-text">Join one of our free workshops and learn practical steps to grow your company together with peers.</div>
      </div>
      <div class="cta-box">
        <div class="cta-icon"><svg width="22" height="20" viewBox="0 0 22 20"><path d="M11 18S2 12 2 6.5A4.5 4.5 0 0 1 11 4a4.5 4.5 0 0 1 9 2.5C20 12 11 18 11 18z" fill="none" stroke="#fff" stroke-width="1.6"/></svg></div>
        <div class="cta-title">Ask a free<span>INTAKE MEETING</span></div>
        <div class="cta-text">Tell us about your business goals and we will plan a first meeting at no cost to find the best approach.</div>
      </div>
    </div>
  </div>
</section>

<section class="welcome">
  <h2 class="section-title">Welcome to Het Zaakkompas</h2>
  <p class="lead">We help small and medium businesses grow with clear advice on marketing, sales and ICT. Our consultants combine hands-on experience with a structured method, so every step you take is focused and measurable. From first intake to lasting results, we stay close to your team and your ambitions.</p>
</section>

<section class="services">
  <div class="wrap">
    <div class="services-media" role="img" aria-label="Video still of two business partners shaking hands">
      <svg width="70" height="70" viewBox="0 0 70 70"><circle cx="35" cy="35" r="33" fill="#fff" opacity=".92"/><path d="M28 22l20 13-20 13z" fill="#3277b5"/></svg>
    </div>
    <div class="services-copy">
      <h3>Our services</h3>
      <p class="strong">We guide growing companies through every stage of their development, with advice tailored to your market.</p>
      <p>Our marketing support helps you reach the right customers with a clear message. In sales we sharpen your process and coach your team to close more deals with confidence and consistency.</p>
      <p>On the ICT side we select and implement tools that save time and fit the way you work, keeping your systems simple, secure and ready for growth.</p>
      <a class="btn" href="#">Read more info</a>
    </div>
  </div>
</section>

<section class="info-band">
  <div class="wrap">
    <div class="info-col">
      <h4>Who we are ?</h4>
      <p>We are a team of three experienced consultants who share a passion for entrepreneurship. Each of us brings years of practice in marketing, sales or ICT to every project.</p>
      <a href="#">Read more info ›</a>
    </div>
    <div class="info-divider"></div>
    <div class="info-col right">
      <h4>How we work ?</h4>
      <p>We start with a free intake, map your goals and build a practical plan. Then we work alongside your team and review results together at every step.</p>
      <a href="#">Read more info ›</a>
    </div>
  </div>
</section>

<section class="offer">
  <h2 class="section-title">We offer consulting services towards SMB</h2>
  <p class="lead">Three areas of expertise, one clear goal: helping your business grow. Discover how our consultants can support you in each field.</p>
  <div class="wrap" style="height:auto">
    <div class="offer-grid">
      <div class="offer-card">
        <div class="offer-photo" role="img" aria-label="Photo of a marketing team discussing a plan"></div>
        <h5>Marketing</h5>
        <p>Build a strong brand and reach the right audience with a focused marketing plan that fits your budget.</p>
      </div>
      <div class="offer-card">
        <div class="offer-photo" role="img" aria-label="Photo of a sales meeting around a table"></div>
        <h5>Sales</h5>
        <p>Improve your sales process and coach your people to win more customers and keep them for longer.</p>
      </div>
      <div class="offer-card">
        <div class="offer-photo" role="img" aria-label="Photo of colleagues working together at a laptop"></div>
        <h5>ICT</h5>
        <p>Choose and implement the right digital tools so your team works smarter, faster and more securely.</p>
      </div>
    </div>
  </div>
</section>

<footer class="site-footer">
  <div class="wrap">
    <div class="foot-col testimonial">
      <h6>Testimonials</h6>
      <p class="quote">Working with this team gave our company a clear direction. Their advice on sales and marketing doubled our leads within one year.</p>
      <div class="author"><div class="avatar"></div><div><b>Lotte Verhaegen</b><span>Managing director</span></div></div>
    </div>
    <div class="foot-col col-welcome">
      <h6>Welcome</h6>
      <ul><li>Home</li><li>Who we are</li><li>How we work</li><li>Skills</li><li>Groeiateliers</li><li>Blog</li><li>Contact us</li></ul>
    </div>
    <div class="foot-col col-info">
      <h6>Information</h6>
      <ul><li>Privacy policy</li><li>Terms &amp; conditions</li><li>Sitemap</li></ul>
    </div>
    <div class="foot-col col-follow">
      <h6>Follow us</h6>
      <ul><li><span class="dot"></span>Community</li><li><span class="dot"></span>Updates</li><li><span class="dot"></span>Network</li><li><span class="dot"></span>Events</li></ul>
    </div>
  </div>
</footer>
<div class="footer-bottom">© 2015 Het Zaakkompas. All rights reserved.</div>

</body>
</html>
```